Beer Label/Realtor Promotion

I'm a Realtor in Vancouver, BC. I'm also a home brewer (of beer). As a gift to my clients, I'll be dropping off 3-6 750ml bottles of beer to their front door periodically. I'll need a label that will be used as a standard bottle label for all bottles, in addition to a neck sticker label that I'll adhere to the neck of the bottle. The neck sticker will be my contact info and real estate info, while the label needs to be something edgy and eye catching. I've included my business card, which may be useful for creative ideas and txt that will likely go on the label. I've included a picture of the pint glasses that were made for me in the past, personal photos of myself and my current business card. Feel free to leverage the design style on this glass as a basis for the design, or do something completely different. I've included a past design created for a magazine that may also be useful as a template.

Dimensions and label ideas can be found here:
http://www.brewmintly.com/post/oval-label-templates

A few ideas: This beer will be a pale ale. One idea was to name it or use the term "Open House Amber", maybe on a homequill for sale sign or something similar.

Another idea was to use personal photos of myself (which I've attached), one from the 90's and one from present day, using a caption like "Keeping your Real Estate and Beer needs in mind since the 90's"...or...Keeping it REAL Estate friendly since the 90's" or any other clever copy.

Target Market(s)

Targeting existing clients and potential real estate clients.

Industry/Entity Type

Real Estate

Requirements
Must have
• Edginess, creativity

```html
<!DOCTYPE html>
<html lang="en">
<head>
<meta charset="utf-8">
<title>Front Step Ale – Bottle &amp; Neck Labels</title>
<link rel="stylesheet" href="https://fonts.googleapis.com/css2?family=Inter:wght@800&display=swap">
<style>
  :root {
    --paper: #ffffff;
    --label-grey: #636363;
    --hop-green: #6bbf3f;
    --sky-blue: #5bc3e4;
    --line-white: #ffffff;
    --photo-dark: #3a3a3a;
    --photo-light: #cfcfcf;
  }
  html, body {
    margin: 0;
    padding: 0;
    overflow: hidden;
    background: var(--paper);
  }
  .artboard {
    display: block;
    width: 1200px;
    height: 1000px;
    background: var(--paper);
  }
  .brand-name {
    font-family: "Inter", "Helvetica Neue", Arial, sans-serif;
    font-weight: 800;
    fill: var(--hop-green);
  }
  .neck-name {
    font-family: "Inter", "Helvetica Neue", Arial, sans-serif;
    font-weight: 800;
    fill: var(--sky-blue);
  }
  .label-body { fill: var(--label-grey); }
  .trim-line { stroke: var(--line-white); stroke-width: 2; fill: none; }
  .over-photo { opacity: 0.8; }
  .wheat-spot { fill: #ffffff; opacity: 0.18; }
</style>
</head>
<body>
<svg class="artboard" viewBox="0 0 1200 1000" xmlns="http://www.w3.org/2000/svg">
  <defs>
    <path id="neck-shape" d="M335 22 Q590 80 835 22 Q855 18 862 34 L912 180 Q918 198 900 203 Q590 330 282 203 Q262 198 268 180 L318 34 Q324 20 335 22 Z"/>
    <clipPath id="neck-clip"><use href="#neck-shape"/></clipPath>
    <clipPath id="oval-clip"><rect x="35" y="290" width="555" height="625" rx="200" ry="260"/></clipPath>
    <linearGradient id="photo-tones" x1="0" y1="0" x2="1" y2="1">
      <stop offset="0" stop-color="var(--photo-light)"/>
      <stop offset="0.55" stop-color="#8a8a8a"/>
      <stop offset="1" stop-color="var(--photo-dark)"/>
    </linearGradient>

    <g id="label-name" class="brand-name">
      <text x="150" y="430" font-size="88" textLength="320" lengthAdjust="spacingAndGlyphs">FRONT</text>
      <text x="150" y="525" font-size="88" textLength="320" lengthAdjust="spacingAndGlyphs">STEP</text>
      <text x="150" y="620" font-size="88" textLength="320" lengthAdjust="spacingAndGlyphs">ALE</text>
      <text x="150" y="715" font-size="88" textLength="320" lengthAdjust="spacingAndGlyphs">SINCE</text>
      <text x="150" y="810" font-size="88" textLength="320" lengthAdjust="spacingAndGlyphs">1998</text>
    </g>
  </defs>

  <g class="neck-label">
    <use href="#neck-shape" class="label-body"/>
    <g clip-path="url(#neck-clip)">
      <circle class="trim-line" cx="590" cy="156" r="152"/>
      <g role="img" aria-label="Crossed wheat stalks ornament">
        <rect class="wheat-spot" x="470" y="70" width="22" height="170" rx="11" transform="rotate(-32 481 155)"/>
        <rect class="wheat-spot" x="688" y="70" width="22" height="170" rx="11" transform="rotate(32 699 155)"/>
      </g>
    </g>
    <text class="neck-name" x="583" y="114" font-size="34" text-anchor="middle" textLength="110" lengthAdjust="spacingAndGlyphs">FRONT</text>
    <text class="neck-name" x="583" y="152" font-size="34" text-anchor="middle" textLength="90" lengthAdjust="spacingAndGlyphs">STEP</text>
  </g>

  <g class="photo-label" clip-path="url(#oval-clip)">
    <rect x="35" y="290" width="555" height="625" fill="url(#photo-tones)" role="img" aria-label="Black and white portrait photo of the realtor from the 1990s"/>
    <use href="#label-name" class="over-photo"/>
  </g>

  <g class="plain-label">
    <rect class="label-body" x="610" y="290" width="555" height="625" rx="200" ry="260"/>
    <line class="trim-line" x1="752" y1="323" x2="1025" y2="323"/>
    <line class="trim-line" x1="752" y1="882" x2="1025" y2="882"/>
    <line class="trim-line" x1="660" y1="410" x2="660" y2="800"/>
    <line class="trim-line" x1="1113" y1="410" x2="1113" y2="800"/>
    <use href="#label-name" transform="translate(575 0)"/>
  </g>
</svg>
</body>
</html>
```